Tidewell Recovery Business Card Design

Professional and clean design. The design colors should flow with the logo. Two-sided card with the website on the back which is:

www.TidewellRecovery.example.

"Specializing in Water Damage Restoration"

On the front I need the name, email, phone, and logo.

Name: Dorian Vashti
Email: Dorian@TidewellRecovery.example
Phone: 555-318-2046 for now

I only have the Preview and Thumbnail right now but should have the source files uploaded within a day or two.

Target Market(s)

Flood victims, home owners with water damage from busted pipes etc...

Industry/Entity Type

Business

Contact Information for Business Card

Name: Dorian Vashti

Font styles to use
Serif
Sans Serif

```html
<!DOCTYPE html>
<html lang="en">
<head>
<meta charset="utf-8">
<title>Tidewell Recovery Business Card</title>
<link href="https://fonts.googleapis.com/css2?family=Cinzel:wght@500&family=Open+Sans:wght@400;700&family=Arimo:wght@400&display=swap" rel="stylesheet">
<style>
  :root {
    --bg: #d9dcdf;
    --brand-blue: #2a9ad6;
    --brand-light: #5cc3ef;
    --white: #ffffff;
    --ink-blue: #2a8fc8;
  }
  * { margin: 0; padding: 0; box-sizing: border-box; }
  html, body { width: 1200px; height: 900px; overflow: hidden; }
  body {
    background: var(--bg);
    position: relative;
    font-family: "Open Sans", sans-serif;
  }
  .card {
    position: absolute;
    width: 560px;
    height: 320px;
    border-radius: 22px;
    overflow: hidden;
    left: 320px;
    box-shadow: 0 6px 18px rgba(0,0,0,0.18);
  }
  /* Back side */
  .card-back {
    top: 100px;
    background: var(--brand-blue);
    color: var(--white);
  }
  .card-back .mark-circle {
    position: absolute;
    left: 50%;
    top: 40px;
    width: 118px;
    height: 118px;
    margin-left: -59px;
    border-radius: 50%;
    background: var(--white);
  }
  .card-back .brand-name {
    position: absolute;
    top: 172px;
    width: 100%;
    text-align: center;
    font-family: "Cinzel", serif;
    font-weight: 500;
    font-size: 22px;
    letter-spacing: 2px;
    color: var(--white);
  }
  .card-back .tagline {
    position: absolute;
    top: 222px;
    width: 100%;
    text-align: center;
    font-family: "Arimo", sans-serif;
    font-size: 15px;
    letter-spacing: 0.6px;
    text-transform: uppercase;
  }
  .card-back .web-rule {
    position: absolute;
    top: 250px;
    left: 80px;
    right: 80px;
    display: flex;
    align-items: center;
    gap: 8px;
    font-family: "Arimo", sans-serif;
    font-size: 15px;
  }
  .card-back .web-rule::before,
  .card-back .web-rule::after {
    content: "";
    flex: 1;
    height: 1px;
    background: var(--white);
  }
  .card-back .edge-line {
    position: absolute;
    left: 0; right: 0;
    bottom: 22px;
    height: 1px;
    background: rgba(255,255,255,0.8);
  }
  /* Front side */
  .card-front {
    top: 480px;
    background: var(--white);
  }
  .card-front .wave { position: absolute; inset: 0; }
  .card-front .brand {
    position: absolute;
    left: 20px;
    top: 96px;
    width: 230px;
    text-align: center;
  }
  .card-front .brand .mark-circle {
    width: 58px;
    height: 58px;
    border-radius: 50%;
    background: var(--ink-blue);
    margin: 0 auto 12px;
  }
  .card-front .brand-name {
    font-family: "Cinzel", serif;
    font-weight: 500;
    font-size: 26px;
    line-height: 1.15;
    letter-spacing: 1px;
    color: var(--ink-blue);
  }
  .card-front .contact {
    position: absolute;
    right: 22px;
    top: 122px;
    text-align: right;
    color: var(--white);
  }
  .card-front .person-name {
    font-weight: 700;
    font-size: 20px;
    letter-spacing: 0.8px;
    text-transform: uppercase;
    margin-bottom: 8px;
  }
  .card-front .contact-line {
    display: flex;
    justify-content: flex-end;
    align-items: center;
    gap: 6px;
    font-size: 12.5px;
    line-height: 19px;
  }
  .card-front .contact-line svg { width: 11px; height: 11px; flex: none; }
</style>
</head>
<body>

  <section class="card card-back" aria-label="Card back">
    <div class="mark-circle"></div>
    <div class="brand-name">Tidewell Recovery</div>
    <p class="tagline">Specializing in Water Damage Restoration</p>
    <p class="web-rule">www.TidewellRecovery.example</p>
    <div class="edge-line"></div>
  </section>

  <section class="card card-front" aria-label="Card front">
    <svg class="wave" viewBox="0 0 560 320" preserveAspectRatio="none">
      <defs>
        <path id="swoosh" d="M560,44 C420,30 320,57 275,140 C240,215 190,286 0,288 L0,320 L560,320 Z"/>
      </defs>
      <use href="#swoosh" fill="var(--brand-light)" transform="translate(-16,-8)"/>
      <use href="#swoosh" fill="var(--white)" transform="translate(-7,-3)"/>
      <use href="#swoosh" fill="var(--brand-blue)"/>
    </svg>

    <div class="brand">
      <div class="mark-circle"></div>
      <div class="brand-name">Tidewell Recovery</div>
    </div>

    <div class="contact">
      <div class="person-name">Dorian Vashti</div>
      <div class="contact-line">555-318-2046
        <svg viewBox="0 0 24 24"><path fill="currentColor" d="M6.6 10.8a15 15 0 0 0 6.6 6.6l2.2-2.2c.3-.3.7-.4 1-.2 1.1.4 2.3.6 3.6.6.6 0 1 .4 1 1V20c0 .6-.4 1-1 1A17 17 0 0 1 3 4c0-.6.4-1 1-1h3.5c.6 0 1 .4 1 1 0 1.3.2 2.5.6 3.6.1.3 0 .7-.2 1z"/></svg>
      </div>
      <div class="contact-line">Dorian@TidewellRecovery.example
        <svg viewBox="0 0 24 24"><rect x="2" y="5" width="20" height="14" rx="2" fill="none" stroke="currentColor" stroke-width="2.4"/><path d="M3 6l9 7 9-7" fill="none" stroke="currentColor" stroke-width="2.4"/></svg>
      </div>
      <div class="contact-line">www.TidewellRecovery.example
        <svg viewBox="0 0 24 24"><circle cx="12" cy="12" r="10" fill="none" stroke="currentColor" stroke-width="2.2"/><path d="M2 12h20M12 2c3 3 3 17 0 20M12 2c-3 3-3 17 0 20" fill="none" stroke="currentColor" stroke-width="1.8"/></svg>
      </div>
    </div>
  </section>

</body>
</html>
```